Profile Card Layout/Design Template

We recently ran a workshop with a client and during that workshop we developed some typical profiles of their target audience using flip chart paper. We now want to turn the profiles into professionally designed A5 cards we can then print and give to the client, therefore we require the profile card layout template to be designed so that in the future we can insert the profile data and images in-house.
Attached are 3 files.
1. persona_sallysocial.jpg is one of profiles we want to convert
2. profilecards.png is an example of the type of design/layout we need to convert the flip chart data to.
3. our company logo
So the layout needs to provide space for
- the profile data specified in persona_sallysocial.jpg
- some additional space for a profile summary/overview not currently shown in persona_sallysocial.jpg but
- an image/photo of the profiled person
- a placeholder for the clients logo
- a placeholder for our company logo
- placeholders for appropriate images to compliment the profile
Happy to consider both portrait and landscape designs
Would be good but not essential if we could change colours of specific elements of the design to compliment the clients corporate colours. So for instance our current clients corporate colours are #b50700, #001739 & #000000

```html
<!DOCTYPE html>
<html lang="en">
<head>
<meta charset="utf-8">
<title>Profile Card – Sally Social</title>
<link rel="stylesheet" href="https://fonts.googleapis.com/css2?family=Catamaran:wght@400;500;600;700&display=swap">
<style>
  :root {
    --brand-red: #b3262c;
    --brand-navy: #0b1838;
    --accent-green: #8dc63f;
    --panel-text: #ffffff;
    --page-bg: #ffffff;
    --card-bg: #f2f2f2;
    --icon-ink: #0b1838;
    --frame-line: #2a2a2a;
  }
  * { box-sizing: border-box; margin: 0; padding: 0; }
  html, body { width: 895px; height: 1200px; overflow: hidden; background: var(--page-bg); }
  body { position: relative; font-family: "Catamaran", "Helvetica Neue", Arial, sans-serif; }

  .profile-card {
    position: absolute; left: 90px; top: 90px; width: 700px; height: 1000px;
    background: var(--card-bg); border: 1px solid var(--frame-line); overflow: hidden;
  }
  .sidebar {
    position: absolute; left: 0; top: 0; width: 238px; height: 100%;
    background: var(--brand-red);
  }
  .sidebar-stripe {
    position: absolute; left: 238px; top: 0; width: 12px; height: 100%;
    background: var(--accent-green);
  }
  .portrait-frame {
    position: absolute; left: 18px; top: 24px; width: 252px; height: 288px;
    background: #ffffff; transform: rotate(-3deg);
    box-shadow: 2px 4px 8px rgba(0,0,0,.35); padding: 14px 14px 44px;
  }
  .portrait-photo {
    width: 100%; height: 100%;
    background: linear-gradient(160deg, #3a2a20 0%, #c9a77a 45%, #e7cfa8 60%, #5a4030 100%);
  }
  .persona-name {
    position: absolute; left: 22px; top: 348px;
    color: var(--accent-green); font-weight: 700; font-size: 26px; line-height: 1;
  }
  .persona-bio {
    position: absolute; left: 22px; top: 382px; width: 196px;
    color: #ffffff; font-size: 15.5px; line-height: 23.2px; font-weight: 500;
  }
  .logo-slot { position: absolute; left: 22px; color: #ffffff; }
  .logo-slot .logo-name { font-weight: 700; font-size: 14px; letter-spacing: .3px; line-height: 1.1; display: flex; align-items: center; gap: 6px; }
  .logo-slot .logo-name::after { content: ""; width: 10px; height: 10px; border-radius: 50%; background: #ffffff; }
  .logo-slot .logo-tag { font-size: 11px; line-height: 1.3; }
  .agency-logo { top: 870px; }
  .client-logo { top: 930px; }

  .stopwatch-image {
    position: absolute; left: 188px; top: 766px; width: 142px; height: 144px; border-radius: 50%;
    background: radial-gradient(circle at 45% 45%, #ffffff 0%, #e4e4e4 55%, #9a9a9a 80%, #c8c8c8 100%);
  }
  .family-image {
    position: absolute; left: 291px; top: 822px; width: 232px; height: 170px;
    background: linear-gradient(180deg, #f3f3f3 0%, #d9cfc8 35%, #c93b3b 70%, #9e1f23 100%);
    border-radius: 10px;
  }
  .shoes-image {
    position: absolute; left: 531px; top: 785px; width: 168px; height: 196px;
    background: linear-gradient(160deg, #e9eef3 0%, #7fa9d6 45%, #2f6fb7 70%, #dfe4ea 100%);
    border-radius: 30px;
  }

  .trait-icon { position: absolute; left: 312px; width: 40px; height: 40px; }
  .trait-panel {
    position: absolute; left: 362px; width: 338px;
    background: var(--brand-navy); color: var(--panel-text);
    padding: 6px 10px 0 10px;
    border-bottom: 4px solid #d7dbe2;
  }
  .trait-panel h2 { font-weight: 600; font-size: 25px; line-height: 30px; margin-bottom: 4px; }
  .trait-panel p { font-size: 15.5px; line-height: 24px; }
  .trait-panel ul { list-style: none; }
  .trait-panel li { font-size: 15.5px; line-height: 30px; }
  .trait-panel li::before { content: "• "; }

  .goal { top: 64px; height: 92px; }
  .motivation { top: 170px; height: 156px; }
  .behavior { top: 339px; height: 106px; }
  .frustration { top: 454px; height: 185px; }
  .frustration li:nth-child(5) { line-height: 20px; }
  .pain-points { top: 649px; height: 164px; }
</style>
</head>
<body>
<main class="profile-card">
  <aside class="sidebar"></aside>
  <div class="sidebar-stripe"></div>

  <div class="portrait-frame"><div class="portrait-photo" role="img" aria-label="Portrait photo of the profiled person"></div></div>

  <h1 class="persona-name">Sally Social</h1>
  <p class="persona-bio">Singer, performer. Born Marla June Fenwick on March 25, 1942. Her father was Baptist preacher Reverend Harold Dean "H.D." Fenwick, and her mother Loretta Vance Fenwick was a gospel singer. The fourth of two kids, Fenwick's parents separated by the time she was six; four years later, her mom succumbed to a heart attack. Guided by H.D.'s preaching assign&shy;ments, her family relocated to Detroit, Michigan.</p>

  <div class="logo-slot agency-logo">
    <div class="logo-name">BRIGHTPATH WORKS</div>
    <div class="logo-tag">Software Solutions Pvt. Ltd.</div>
  </div>
  <div class="logo-slot client-logo">
    <div class="logo-name">OTHER LOGO</div>
    <div class="logo-tag">Software Solutions Pvt. Ltd.</div>
  </div>

  <div class="stopwatch-image" role="img" aria-label="Photo of a silver stopwatch"></div>
  <div class="family-image" role="img" aria-label="Photo of a family sitting together on a red sofa"></div>
  <div class="shoes-image" role="img" aria-label="Photo of a pair of blue running shoes"></div>

  <svg class="trait-icon" style="top:70px" viewBox="0 0 40 40" fill="none" stroke="var(--icon-ink)" stroke-width="2">
    <path d="M4 6v30h32"/><rect x="9" y="22" width="5" height="12"/><rect x="17" y="16" width="5" height="18"/><rect x="25" y="10" width="5" height="24"/>
  </svg>
  <section class="trait-panel goal">
    <h2>My Goal</h2>
    <p>Have fun being physically active<br>with like-minded people.</p>
  </section>

  <svg class="trait-icon" style="top:176px" viewBox="0 0 40 40" fill="none" stroke="var(--icon-ink)" stroke-width="2.2" stroke-linejoin="round">
    <rect x="3" y="18" width="7" height="16"/><path d="M10 20l7-6 3-10c3 0 4 3 3 7l-1 5h11c2 0 3 2 2 4l-3 12c-1 2-2 2-4 2H10"/>
  </svg>
  <section class="trait-panel motivation">
    <h2>My Motivation</h2>
    <ul><li>Friendship/Relationship</li><li>Making the most of every moment</li><li>Value for money</li><li>Well organized</li></ul>
  </section>

  <svg class="trait-icon" style="top:345px" viewBox="0 0 40 40" fill="none" stroke="var(--icon-ink)" stroke-width="2.2">
    <circle cx="20" cy="20" r="17"/><circle cx="14" cy="15" r="1.5" fill="var(--icon-ink)"/><path d="M24 15h4"/><path d="M11 23c3 6 15 6 18 0"/>
  </svg>
  <section class="trait-panel behavior">
    <h2>My Behavior</h2>
    <ul><li>Busy</li><li>No flashy technology</li></ul>
  </section>

  <svg class="trait-icon" style="top:460px" viewBox="0 0 40 40" fill="none" stroke="var(--icon-ink)" stroke-width="2.2">
    <circle cx="20" cy="20" r="17"/><path d="M11 15l5 2M29 15l-5 2"/><path d="M11 28c3-3 6-3 9 0s6 3 9 0"/>
  </svg>
  <section class="trait-panel frustration">
    <h2>My Frustration/Fear</h2>
    <ul><li>Doesn't like down time</li><li>Too competitive</li><li>Wasting any time</li><li>Who's looking after the kids?</li><li>I won't be able to play?</li></ul>
  </section>

  <svg class="trait-icon" style="top:655px" viewBox="0 0 40 40" fill="none" stroke="var(--icon-ink)" stroke-width="2.2">
    <circle cx="20" cy="20" r="15"/><path d="M12 16l5 1M28 16l-5 1"/><path d="M13 28c3-4 11-4 14 0"/><path d="M3 22v6M37 22v6"/>
  </svg>
  <section class="trait-panel pain-points">
    <h2>My Pain Points</h2>
    <ul><li>Things just must work-functional</li><li>You won't be good enough</li><li>Scared of being hurt</li><li>Knowledge of rules</li></ul>
  </section>
</main>
</body>
</html>
```